COMPANY NAME: Bright Harbor Outlooks: Task Description: We are a new UK based business with global rea

Target Market

- Personal and professional development – 30-55 age group, corporate leaders, Eastern European and Asian markets
- On-assignment projects – Corporate market – Eastern European and Asian Markets
- Property investment - 35-65 age group, Europe, USA, Australia

What we need

We need logos and brand design for a suite of web platforms (website, twitter and Facebook profile). We would like to have a cohesive and consistent look across all of our online platforms. The design suite must therefore include social media logos, backgrounds and headers. Specifically we are looking for:

a. Facebook header/page design: likely to have a more youthful look

b. Website: Header, background and layout that is responsive to devices, iPhone primarily, then tablet, then PC (we have purchased a website building package from WebNimbus so if you are familiar with one of their themes, it would be great to have a design that fits with a theme you would recommend); Design should be able to accommodate a place to position video in the medium term but an image in the short term.

c. LinkedIn: header/logo; more corporate look

d. Twitter: background/logo

e. Powerpoint template: background and logo - simple and soft background not busy

f. Electronic Newsletter: logo, header and sidebar; simple and soft background not busy

h. Business card: sophisticated and simple

Colors

We have in mind a preference for colors from the purple family, maybe lavender, so as to appeal to all genders and age groups. Though we are happy to go with a recommendation if you think otherwise.

We would like a look that is professional, airy, bright, fresh, futuristic, insightful, friendly.

Ethos of the brand

- experiencing opportunity and being fulfilled in a changing world
- services are facilitated through insights
- support provided through our product, services and tailored approach to coaching/partnerships (which includes private client match-making)
- we are service providers and passionate about quality and modern leadership skills at all stages in life.

The company name is "Bright Harbor Outlooks” - our main message is helping people move to the next level - through investments, personal and professional growth.

Some of our messaging

1. International Leadership in a new world.

2. New technology;

3. Informed;

4. Positively Influential

5. Making a difference;

6. Empowered;

7. Risk free investments;

8. Commercial opportunity;

9. Fulfilled living;

10. Carefree and Fun Living;

11. Progression;

12. Open-minded

13. Energy/dynamic

The Business:
The business is to move people very quickly out of situations that hold them back. the situations could be their own personal situations; their career; their jobs; their teams; their ideas; their finances; their financial opportunities. Remove their fears and give them the strategies to take action. The team are international and have 40 years experience between them in this area.

We do want to come across modern and dynamic, customer outcome focussed, building long-term relationships; international.
Updates

Project Deadline Extended
Reason: We have not found the right designs - we are not just looking for a website design but also images and logos. Most images we can see in the designs are stock images - very standard. We need an image which will be the face of the company, like the shop front window. This main image will be used on social media (top image) and also the home page of the website.

Target Market(s)

30-55 years
Eastern Europe; UK; Asia; Africa; Middle East
Personal, Professional, Corporate, and Financial Growth

Industry/Entity Type

Business Service

Contact Information for Business Card

Simple and stylish
the 3 areas of the business on the reverse -

International look - Offices in UK and San Francisco

Company name
web address www.brightharboroutlook.example
email director@brightharboroutlook.example
Facebook bright harbor outlook
LinkedIn Bright Harbor Outlook
Twitter Bright Harbor Outlook
Telephone: +44 (0) 700 900 0123

Logo Text

Something that symbolises unlimited growth - probably not text - could use the word INSIGHT in some way

Number of Pages Required

1 page

Colors
e4daeb
f3f1f8
ffffff

Requirements
Must have
• social media symbols and address
• company name
• Marianne Tolley
• Director
• Telephone +44 (0) 700 900 0123
• Website name www.brightharboroutlook.example.uk
• Reverse of Card:
• Discreet, Fast, Bright Harbor Consultancy
• Corporate, Professional, Personal & Property Investment
Nice to have
• not too angular; soft lines; not too cluttered (possibly social media on the reverse and just logo, name, number on the front?
Should not have
• too busy

```html
<!DOCTYPE html>
<html lang="en">
<head>
<meta charset="utf-8">
<title>Bright Harbor Outlook</title>
<link rel="stylesheet" href="https://fonts.googleapis.com/css2?family=Montserrat:ital,wght@0,400;0,600;0,700;1,700&family=Open+Sans:wght@400;600;700&display=swap">
<style>
:root{
  --purple:#8e2a8c;
  --purple-deep:#6d1f6d;
  --violet:#9a34f0;
  --lavender:#e4daeb;
  --mist:#f3f1f8;
  --ink:#333;
  --text:#555;
  --dark:#1d1d1d;
  --darker:#111;
  --navy:#2c4a74;
  --frame:#e6e6e6;
  --white:#fff;
}
*{box-sizing:border-box;margin:0;padding:0}
html,body{width:1200px;height:3203px;overflow:hidden}
body{background:var(--frame);font-family:"Open Sans",Arial,sans-serif;color:var(--text)}
.page{width:1170px;margin:0 15px;height:3203px;background:var(--white);position:relative}
section,header,footer{position:relative;overflow:hidden}

/* Hero */
.hero{height:737px;background:#1a1a22}
.hero-photo{position:absolute;inset:0;background:linear-gradient(180deg,#2b2f45 0%,#5a4a55 35%,#b78650 52%,#3a3238 70%,#17161a 100%)}
.hero-shade{position:absolute;left:0;right:0;bottom:0;height:190px}
.contact-bar{position:absolute;top:10px;left:583px;width:555px;height:42px;background:var(--purple);border-radius:0 0 4px 4px;display:flex;align-items:center;gap:26px;padding:0 20px;color:var(--white);font-size:13px;font-weight:600}
.contact-bar .item{display:flex;align-items:center;gap:8px}
.social{display:flex;gap:5px;margin-left:auto}
.social span{width:18px;height:18px;border:1.5px solid var(--white);border-radius:50%}
.brand{position:absolute;top:62px;left:28px;font-family:"Montserrat",sans-serif;font-weight:700;font-size:27px;color:#b5479f;letter-spacing:.5px}
.nav{position:absolute;top:78px;left:593px;display:flex;gap:28px;font-family:"Montserrat",sans-serif;font-size:13px;font-weight:700;color:var(--white)}
.nav a{color:inherit;text-decoration:none;padding-bottom:7px}
.nav a.active{color:#e3a0ee;border-bottom:3px solid var(--purple)}
.hero-title{position:absolute;top:268px;left:0;right:0;text-align:center;font-family:"Montserrat",sans-serif;font-weight:700;color:var(--white);text-transform:uppercase;text-shadow:0 2px 6px rgba(0,0,0,.5)}
.hero-title .l1{font-size:32px;letter-spacing:.5px}
.hero-title .l2{font-size:39px;margin-top:4px}
.hero-title em{font-style:normal;color:#c35ed6}
.hero-rule{width:430px;height:1px;background:rgba(255,255,255,.6);margin:8px auto 0}
.services{position:absolute;top:558px;left:0;right:0;display:flex;justify-content:center;gap:98px}
.service{width:200px;text-align:center;color:var(--white);font-family:"Montserrat",sans-serif;font-size:14px;font-weight:600}
.service:nth-child(2){margin-top:10px}
.service .badge{width:92px;height:92px;margin:0 auto 14px;border-radius:50%;background:var(--purple);border:5px solid #c35ed6;display:flex;align-items:center;justify-content:center;box-shadow:0 0 0 6px rgba(0,0,0,.25)}
.service .badge span{width:64px;height:64px;border-radius:50%;background:#1d1d1d;display:flex;align-items:center;justify-content:center}

/* Headings */
.sec-head{text-align:center;font-family:"Montserrat",sans-serif;font-size:25px;font-weight:400;color:var(--ink);text-transform:uppercase}
.sec-head em{font-style:italic;font-weight:700;color:var(--purple)}
.divider{width:670px;height:24px;margin:10px auto 0;position:relative}
.divider::before{content:"";position:absolute;left:0;right:0;top:8px;height:1px;background:#ccc}
.divider::after{content:"";position:absolute;left:324px;top:2px;width:20px;height:20px;border-radius:50%;background:var(--white);border:3px solid #bbb}
.on-purple .sec-head,.on-purple .sec-head em{color:var(--white)}
.on-purple .divider::before{background:rgba(255,255,255,.6)}
.on-purple .divider::after{background:transparent;border-color:var(--white)}

/* About */
.about{height:476px;padding-top:64px}
.about-copy{width:900px;margin:44px auto 0;text-align:center;font-size:13.5px;line-height:20px;color:var(--text)}
.about-copy p{margin-bottom:18px}
.btn{display:inline-block;background:var(--purple);color:var(--white);font-family:"Montserrat",sans-serif;font-weight:700;font-size:13.5px;text-transform:uppercase;padding:8px 26px;border-radius:3px}
.about .btn{margin-top:4px}

/* Consultancy */
.consultancy{height:602px;background:linear-gradient(135deg,#9b3d9a 0%,#8a2c88 50%,#b15db0 100%);padding-top:58px}
.cards{position:absolute;top:145px;left:41px;display:flex;gap:19px}
.card{width:350px;height:403px;background:var(--white);position:relative;box-shadow:0 3px 8px rgba(0,0,0,.25)}
.card .photo{height:158px}
.card p{padding:20px 16px 0;font-size:13px;line-height:18.5px;color:var(--ink)}
.card .tab{position:absolute;left:0;right:0;bottom:0;height:70px}
.card .tab svg{position:absolute;inset:0}
.card .tab b{position:absolute;left:0;right:0;bottom:10px;text-align:center;color:var(--white);font-family:"Montserrat",sans-serif;font-size:16.5px;font-weight:700}

/* Testimonials */
.testimonials{height:416px;padding-top:58px}
.quote{position:absolute;top:143px;left:241px;width:690px;height:145px;background:var(--mist);border:1px solid #ddd;border-radius:6px;box-shadow:0 2px 5px rgba(0,0,0,.12);padding:18px 24px 0 58px;font-size:12.5px;line-height:19px;color:var(--text)}
.quote .mark{position:absolute;font-family:Georgia,serif;font-size:54px;font-weight:700;color:#444;line-height:1}
.quote .open{left:16px;top:8px}
.quote .close{left:148px;bottom:-18px}
.quote::after{content:"";position:absolute;left:28px;bottom:-13px;width:22px;height:22px;background:var(--mist);border-right:1px solid #ddd;border-bottom:1px solid #ddd;transform:rotate(45deg)}
.cite{position:absolute;top:305px;left:241px;font-style:italic;font-weight:700;font-size:15px;color:var(--ink)}
.dots{position:absolute;top:350px;left:0;right:0;display:flex;justify-content:center;gap:4px}
.dots span{width:12px;height:12px;border-radius:50%;border:1.5px solid #999}
.dots span.on{background:var(--purple);border-color:var(--purple)}

/* News */
.news{height:651px;background:linear-gradient(135deg,#a85aa8 0%,#8d2f8b 45%,#b066b0 100%);padding-top:62px}
.news-feature{position:absolute;top:164px;left:77px;width:324px;height:427px;background:var(--white);box-shadow:0 3px 8px rgba(0,0,0,.25)}
.news-feature .photo{height:176px}
.news-feature h3{padding:22px 22px 0;font-family:"Montserrat",sans-serif;font-size:33px;font-weight:700;color:var(--ink)}
.news-feature p{padding:18px 22px 0;font-size:13.5px;line-height:19px;color:var(--ink)}
.news-feature .btn{position:absolute;left:70px;bottom:20px;width:185px;text-align:center;background:var(--violet);text-transform:none;font-weight:600;font-size:16px;padding:6px 0;border-radius:0}
.news-item{position:absolute;width:325px;height:198px;background:var(--white);box-shadow:0 3px 8px rgba(0,0,0,.25)}
.news-item .photo{height:158px}
.news-item .bar{height:40px;display:flex;align-items:center;justify-content:space-between;padding-left:14px}
.news-item h4{font-family:"Montserrat",sans-serif;font-size:17px;font-weight:700;color:var(--ink)}
.news-item .more{background:var(--violet);color:var(--white);font-size:14px;height:32px;line-height:32px;padding:0 16px;margin-top:-6px;align-self:flex-start}
.date{position:absolute;top:-14px;left:-14px;width:92px;height:92px;border-radius:50%;background:var(--navy);border:3px solid var(--white);box-shadow:0 0 0 3px rgba(44,74,116,.6);color:var(--white);text-align:center;font-family:"Montserrat",sans-serif;font-weight:700;padding-top:11px;z-index:2}
.date .m{font-size:12px;display:block}
.date .d{font-size:27px;display:block;line-height:1.1;border-top:1px solid rgba(255,255,255,.6);border-bottom:1px solid rgba(255,255,255,.6);margin:1px 14px}
.date .y{font-size:12px;display:block}

/* Footer */
.site-footer{height:278px;background:var(--dark);padding:38px 0 0 74px;color:var(--white);display:flex}
.f-col h5{font-family:"Montserrat",sans-serif;font-size:13px;font-weight:700;color:#b14fc4;text-transform:uppercase;padding-bottom:8px;border-bottom:1px solid #444;margin-bottom:12px}
.f-col ul{list-style:none;font-size:12px;line-height:19px;font-weight:600;text-transform:uppercase}
.f-links{width:85px;margin-right:86px}
.f-assign{width:260px;margin-right:70px}
.f-form{width:220px}
.f-form .field{background:var(--darker);height:26px;margin-bottom:6px;font-size:9.5px;font-weight:700;padding:5px 10px}
.f-form .field.tall{height:58px}
.f-form .submit{display:inline-block;background:var(--darker);font-size:12px;font-weight:700;padding:5px 14px;margin-top:4px}
.f-brand{margin:52px 0 0 68px;text-align:center}
.f-brand .name{font-family:"Montserrat",sans-serif;font-weight:700;font-size:22px;color:#b5479f}
.f-brand .tel{margin-top:30px;display:flex;align-items:center;justify-content:center;gap:10px;font-size:15px;font-weight:600}
.legal{height:43px;background:var(--white);display:flex;align-items:center;padding:0 24px;font-size:9px;font-weight:700;color:#333}
.legal .social{gap:10px}
.legal .social span{width:11px;height:11px;border:1.5px solid #333}
</style>
</head>
<body>
<div class="page">

<header class="hero">
  <div class="hero-photo" role="img" aria-label="Evening photograph of a city riverside with a tower bridge and modern glass building at sunset"></div>
  <svg class="hero-shade" viewBox="0 0 1170 190" preserveAspectRatio="none" aria-hidden="true">
    <path d="M0 60 Q585 -10 1170 40 L1170 190 L0 190 Z" fill="#1b1b1f" opacity=".92"/>
  </svg>
  <div class="contact-bar">
    <span class="item"><svg width="18" height="18" viewBox="0 0 20 20" aria-hidden="true"><circle cx="10" cy="10" r="9" fill="none" stroke="#fff" stroke-width="1.5"/><path d="M6.5 5.5l2 2-1 1.2a6 6 0 0 0 3.8 3.8l1.2-1 2 2-1.3 1.3c-3.5 0-7.9-4.4-7.9-7.9z" fill="#fff"/></svg>+44 (0) 700 900 0123</span>
    <span class="item"><svg width="18" height="18" viewBox="0 0 20 20" aria-hidden="true"><circle cx="10" cy="10" r="9" fill="none" stroke="#fff" stroke-width="1.5"/><rect x="5" y="6.5" width="10" height="7" fill="none" stroke="#fff" stroke-width="1.3"/><path d="M5 6.5l5 4 5-4" fill="none" stroke="#fff" stroke-width="1.3"/></svg>director@brightharboroutlook.example</span>
    <span class="social" aria-label="Social profiles"><span></span><span></span><span></span></span>
  </div>
  <div class="brand">BRIGHT HARBOR OUTLOOK</div>
  <nav class="nav">
    <a class="active">HOME</a><a>ABOUT US</a><a>OUR VALUES</a><a>TESTIMONIALS</a><a>NEWS</a><a>CONTACT</a>
  </nav>
  <h1 class="hero-title">
    <div class="l1">Hello and welcome to the company</div>
    <div class="l2">that <em>works with you</em> on your terms</div>
    <div class="hero-rule"></div>
  </h1>
  <div class="services">
    <div class="service"><div class="badge"><span><svg width="36" height="28" viewBox="0 0 36 28" aria-hidden="true"><g fill="#fff"><circle cx="18" cy="8" r="5"/><path d="M9 26c0-6 4-10 9-10s9 4 9 10z"/><circle cx="7" cy="11" r="3.5"/><path d="M0 25c0-4 3-7 7-7 1.5 0 2.5.4 3 .8-1.5 2-2.5 4-2.5 6.2z"/><circle cx="29" cy="11" r="3.5"/><path d="M36 25c0-4-3-7-7-7-1.5 0-2.5.4-3 .8 1.5 2 2.5 4 2.5 6.2z"/></g></svg></span></div>Team Cohesion Strategy</div>
    <div class="service"><div class="badge"><span><svg width="36" height="36" viewBox="0 0 36 36" aria-hidden="true"><g fill="none" stroke="#fff" stroke-width="3"><circle cx="18" cy="18" r="11"/><path d="M18 2v9M18 25v9M2 18h9M25 18h9"/></g><circle cx="18" cy="18" r="3" fill="#fff"/></svg></span></div>Go To Market Strategy</div>
    <div class="service"><div class="badge"><span><svg width="36" height="36" viewBox="0 0 36 36" aria-hidden="true"><g fill="none" stroke="#fff" stroke-width="2"><circle cx="18" cy="18" r="14"/><ellipse cx="18" cy="18" rx="6" ry="14"/><path d="M4 18h28M6 11h24M6 25h24"/></g></svg></span></div>Internationalisation Strategy</div>
  </div>
</header>

<section class="about">
  <h2 class="sec-head">About <em>Bright Harbor Outlook</em></h2>
  <div class="divider"></div>
  <div class="about-copy">
    <p>If you seek an experienced and trusted partner to work with you on an assignment or simply want some strategies to move your personal or professional talents to the next level then you are in the right place.</p>
    <p>If you feel that the pace of change in business is so fast that to be an outstanding leader you should ensure you are brought up to speed regularly then you are in the right place.</p>
    <p>If you are hearing about the essential new leadership essentials and you are ready to hear how to adopt them into your life or business then you are at the right place.</p>
    <p>I am so convinced that you will be delighted with how fast you can make change happen.</p>
    <span class="btn">More about us</span>
  </div>
</section>

<section class="consultancy on-purple">
  <h2 class="sec-head"><em>Consultancy</em></h2>
  <div class="divider"></div>
  <div class="cards">
    <article class="card">
      <div class="photo" role="img" aria-label="Photo of colleagues talking around a laptop in a bright office" style="background:linear-gradient(135deg,#c9d4dc,#7d8fa0)"></div>
      <p>Lorem ipsum dolor sit amet, consectetuer adipiscing elit, sed diam nonummy nibh euismod tincidunt ut laoreet dolore magna aliquam erat volutpat. Ut wisi enim ad minim veniam, quis nostrud exerci tation ullamcorper suscipit lobortis nisl ut aliquip ex ea commodo consequat.</p>
      <div class="tab"><svg viewBox="0 0 350 70" preserveAspectRatio="none" aria-hidden="true"><path d="M0 30 L175 6 L350 30 L350 70 L0 70Z" fill="#6d1f6d"/><path d="M0 38 L175 16 L350 38 L350 70 L0 70Z" fill="#9a34f0"/></svg><b>Professional and Personal</b></div>
    </article>
    <article class="card">
      <div class="photo" role="img" aria-label="Photo of an audience of young professionals at a business seminar" style="background:linear-gradient(135deg,#aab8c8,#56667a)"></div>
      <p>Lorem ipsum dolor sit amet, consectetuer adipiscing elit, sed diam nonummy nibh euismod tincidunt ut laoreet dolore magna aliquam erat volutpat. Ut wisi enim ad minim veniam, quis nostrud exerci tation ullamcorper suscipit lobortis nisl ut aliquip ex ea commodo consequat.</p>
      <div class="tab"><svg viewBox="0 0 350 70" preserveAspectRatio="none" aria-hidden="true"><path d="M0 30 L175 6 L350 30 L350 70 L0 70Z" fill="#6d1f6d"/><path d="M0 38 L175 16 L350 38 L350 70 L0 70Z" fill="#9a34f0"/></svg><b>Next Generation Leaders (16-30)</b></div>
    </article>
    <article class="card">
      <div class="photo" role="img" aria-label="Photo of a consultant working at a laptop by a window" style="background:linear-gradient(135deg,#d8dde2,#8e9aa6)"></div>
      <p>Lorem ipsum dolor sit amet, consectetuer adipiscing elit, sed diam nonummy nibh euismod tincidunt ut laoreet dolore magna aliquam erat volutpat. Ut wisi enim ad minim veniam, quis nostrud exerci tation ullamcorper suscipit lobortis nisl ut aliquip ex ea commodo consequat.</p>
      <div class="tab"><svg viewBox="0 0 350 70" preserveAspectRatio="none" aria-hidden="true"><path d="M0 30 L175 6 L350 30 L350 70 L0 70Z" fill="#6d1f6d"/><path d="M0 38 L175 16 L350 38 L350 70 L0 70Z" fill="#9a34f0"/></svg><b>Consultation Options</b></div>
    </article>
  </div>
</section>

<section class="testimonials">
  <h2 class="sec-head">Client <em>Testimonials</em></h2>
  <div class="divider"></div>
  <blockquote class="quote">
    <span class="mark open">&ldquo;</span>
    Lorem ipsum dolor sit amet, consectetuer adipiscing elit, sed diam nonummy nibh euismod tincidunt ut laoreet dolore magna aliquam erat volutpat. Ut wisi enim ad minim veniam, quis nostrud exerci tation ullamcorper suscipit lobortis nisl ut aliquip ex ea commodo consequat. Duis autem vel eum iriure dolor in hendrerit in vulputate velit esse molestie consequat, vel illum dolore eu feugiat nulla facilisis at vero.
    <span class="mark close">&rdquo;</span>
  </blockquote>
  <div class="cite">Clara Devon</div>
  <div class="dots"><span class="on"></span><span></span><span></span><span></span></div>
</section>

<section class="news on-purple">
  <h2 class="sec-head">Latest <em>News</em></h2>
  <div class="divider"></div>
  <article class="news-feature">
    <div class="date"><span class="m">AUG</span><span class="d">06</span><span class="y">2016</span></div>
    <div class="photo" role="img" aria-label="Photo of a smiling businessman with colleagues at a laptop" style="background:linear-gradient(135deg,#dfe5ea,#8d9cab)"></div>
    <h3>NEWS TITLE #1</h3>
    <p>Lorem ipsum dolor sit amet, consectetuer adipiscing elit, sed diam nonummy nibh euismod tincidunt ut laoreet dolore magna aliquam erat volutpat. Ut wisi enim ad.</p>
    <span class="btn">Read More</span>
  </article>
  <article class="news-item" style="top:164px;left:431px">
    <div class="date"><span class="m">AUG</span><span class="d">04</span><span class="y">2016</span></div>
    <div class="photo" role="img" aria-label="Photo of a businesswoman leaping over growth charts" style="background:linear-gradient(135deg,#e7ecf2,#9fb0c6)"></div>
    <div class="bar"><h4>News Title #2</h4><span class="more">Read More</span></div>
  </article>
  <article class="news-item" style="top:164px;left:788px">
    <div class="date"><span class="m">AUG</span><span class="d">01</span><span class="y">2016</span></div>
    <div class="photo" role="img" aria-label="Photo of two businessmen reviewing a document" style="background:linear-gradient(135deg,#c5ccd6,#4d5a6c)"></div>
    <div class="bar"><h4>News Title #4</h4><span class="more">Read More</span></div>
  </article>
  <article class="news-item" style="top:395px;left:431px">
    <div class="date"><span class="m">AUG</span><span class="d">02</span><span class="y">2016</span></div>
    <div class="photo" role="img" aria-label="Photo of a hand using a tablet showing a line chart" style="background:linear-gradient(135deg,#cfd6de,#6f7e8e)"></div>
    <div class="bar"><h4>News Title #3</h4><span class="more">Read More</span></div>
  </article>
  <article class="news-item" style="top:395px;left:788px">
    <div class="date"><span class="m">JUL</span><span class="d">28</span><span class="y">2016</span></div>
    <div class="photo" role="img" aria-label="Photo of a businessman using a smartphone" style="background:linear-gradient(135deg,#bcc6d2,#3f4c5e)"></div>
    <div class="bar"><h4>News Title #5</h4><span class="more">Read More</span></div>
  </article>
</section>

<footer class="site-footer">
  <div class="f-col f-links">
    <h5>Quick Links</h5>
    <ul><li>Home</li><li>About Us</li><li>Our Values</li><li>Testimonials</li><li>News</li><li>Contact</li></ul>
  </div>
  <div class="f-col f-assign">
    <h5>On Assignment</h5>
    <ul><li>Team Cohesion Strategy</li><li>Go To Market Strategy</li><li>Internationalisation Strategy</li></ul>
  </div>
  <div class="f-col f-form">
    <h5>Send a Message</h5>
    <div class="field">NAME</div>
    <div class="field">EMAIL</div>
    <div class="field tall">MESSAGE</div>
    <span class="submit">SUBMIT</span>
  </div>
  <div class="f-brand">
    <div class="name">BRIGHT HARBOR OUTLOOK</div>
    <div class="tel"><svg width="24" height="24" viewBox="0 0 20 20" aria-hidden="true"><circle cx="10" cy="10" r="9" fill="none" stroke="#fff" stroke-width="1.5"/><path d="M6.5 5.5l2 2-1 1.2a6 6 0 0 0 3.8 3.8l1.2-1 2 2-1.3 1.3c-3.5 0-7.9-4.4-7.9-7.9z" fill="#fff"/></svg>+44 (0) 700 900 0123</div>
  </div>
</footer>
<div class="legal">COPYRIGHT © 2016 BRIGHT HARBOR OUTLOOK. ALL RIGHTS RESERVED.<span class="social" aria-label="Social profiles"><span></span><span></span><span></span></span></div>

</div>
</body>
</html>
```